homepage design , industry automation control image

we need a design , based on our Logo image.

we focus on selling of temprature sensor ,and parts.

but need concept or image on industry automation control

we need enviroment friendly concept.

Industry/Entity Type

Industry

Number of Pages Required

5+ page

Requirements
Must have
• we need a Cartoon Image of a Temperature sensor,
• attaching a Excel file with the sensor looking.
Nice to have
• Nature image, future concept

```html
<!DOCTYPE html>
<html lang="en">
<head>
<meta charset="utf-8">
<title>Verdant Sensorik – Home</title>
<link href="https://fonts.googleapis.com/css2?family=Raleway:wght@300;400;500;600&family=Roboto:wght@700;900&display=swap" rel="stylesheet">
<style>
  :root{
    --green:#2ea200;
    --green-light:#7ed321;
    --green-dark:#239000;
    --navy:#0b0b6b;
    --ink:#333333;
    --muted:#666666;
    --band:#e6e5ea;
    --footer:#1b1b2d;
    --footer-text:#b9b9c6;
    --white:#ffffff;
  }
  *{margin:0;padding:0;box-sizing:border-box}
  html,body{width:1198px;height:1200px;overflow:hidden;background:var(--white)}
  body{position:relative;font-family:'Raleway',sans-serif;color:var(--ink)}
  .abs{position:absolute}

  /* utility bar */
  .util a{position:absolute;top:18px;font-size:12px;color:var(--ink);text-decoration:none}
  .cart-count{left:1076px;top:14px;width:23px;height:22px;background:var(--navy);color:#fff;font-size:12px;display:flex;align-items:center;justify-content:center}

  /* nav band */
  .navband{left:0;top:48px;width:1198px;height:38px;background:linear-gradient(180deg,var(--green) 0%,var(--green-light) 100%)}
  .brand{left:98px;top:48px;width:223px;height:40px;background:#fff;display:flex;align-items:center;gap:6px;padding-left:12px}
  .brand-square{width:22px;height:22px;background:var(--green)}
  .brand-name{font-family:'Raleway',sans-serif;font-weight:600;font-size:17px;color:var(--green-dark)}
  .nav a{position:absolute;top:61px;font-size:14px;color:#fff;text-decoration:none}
  .nav .active{border-bottom:3px solid var(--navy);padding-bottom:4px}
  .search{left:945px;top:58px;width:154px;height:19px;background:#fff;font-size:10px;color:#999;padding:3px 8px}
  .search svg{position:absolute;right:5px;top:3px}

  /* hero */
  .hero{left:0;top:98px;width:1198px;height:305px;background:linear-gradient(100deg,#6f8f4e 0%,#3f6b2a 30%,#2f8a1a 48%,#3c9a2a 70%,#5ba640 100%)}
  .hero-title{left:614px;top:174px;font-family:'Roboto',sans-serif;font-weight:900;font-size:46px;color:#fff;letter-spacing:.5px}
  .hero-sub{left:618px;top:239px;font-weight:300;font-size:22px;color:#fff;letter-spacing:.5px}

  .band{left:0;top:403px;width:1198px;height:222px;background:var(--band)}
  .card{top:330px;width:314px;height:255px;background:#fff}
  .card-media{position:absolute;left:10px;top:12px;width:294px;height:132px;border:1px solid #cfcfcf;background:linear-gradient(135deg,#ffffff 0%,#e9ecef 55%,#b8bec4 100%)}
  .card h3{position:absolute;left:11px;top:152px;font-family:'Roboto',sans-serif;font-weight:700;font-size:16px;color:var(--ink)}
  .card .rule{position:absolute;left:11px;top:174px;width:40px;height:2px;background:var(--green)}
  .card p{position:absolute;left:11px;top:183px;width:290px;font-size:11px;line-height:13px;color:var(--muted)}
  .btn{position:absolute;left:9px;top:219px;width:135px;height:24px;background:var(--navy);color:#fff;font-size:10px;font-weight:500;display:flex;align-items:center;justify-content:center}

  /* welcome */
  .welcome-media{left:118px;top:672px;width:238px;height:108px;background:linear-gradient(160deg,#7ab4d8 0%,#5a98c4 60%,#a6b9c8 100%);border-radius:6px}
  .welcome h2{position:absolute;left:382px;top:650px;font-weight:300;font-size:27px;color:var(--ink)}
  .welcome .rule{position:absolute;left:383px;top:690px;width:40px;height:2px;background:var(--green)}
  .welcome .lead{position:absolute;left:381px;top:704px;font-size:16px;color:var(--green)}
  .welcome .body{position:absolute;left:384px;top:750px;width:700px;font-size:11.2px;line-height:18px;color:var(--muted)}

  /* newsletter */
  .news{left:0;top:870px;width:1198px;height:116px;background:var(--green)}
  .news-text{left:248px;top:911px;font-size:14px;line-height:17px;color:#fff}
  .email{left:604px;top:906px;width:269px;height:45px;background:#fff;font-size:15px;font-weight:300;color:#999;padding:12px 20px}
  .subscribe{left:885px;top:906px;width:135px;height:45px;background:var(--navy);color:#fff;font-size:14px;display:flex;align-items:center;justify-content:center}

  /* footer */
  .footer{left:0;top:986px;width:1198px;height:214px;background:var(--footer)}
  .flinks{font-size:11.5px;line-height:18px;color:var(--footer-text)}
  .social{font-size:11.5px;color:var(--footer-text)}
  .social span{position:absolute;left:581px}
  .social i{position:absolute;left:560px;width:9px;height:9px;border-radius:50%;background:#fff}
  .call-label{left:836px;top:1016px;font-size:12px;color:var(--footer-text)}
  .call-num{left:836px;top:1031px;font-size:21px;color:#fff}
  .addr{left:842px;top:1085px;font-size:10.5px;line-height:13px;color:var(--footer-text)}
  .divider{left:0;top:1150px;width:1198px;height:1px;background:#2c2c40}
  .copy{left:0;top:1169px;width:1198px;text-align:center;font-size:10px;color:#8a8a98}
</style>
</head>
<body>

<nav class="util">
  <a style="left:868px">My Account</a>
  <a style="left:945px">Delivery</a>
  <a style="left:1002px">Help</a>
  <svg class="abs" style="left:1047px;top:15px" width="20" height="18" viewBox="0 0 20 18" aria-hidden="true">
    <path d="M5 6 L10 1 L15 6" fill="none" stroke="#7ed321" stroke-width="2"/>
    <path d="M1 6 H19 L17 17 H3 Z" fill="#7ed321"/>
    <path d="M7 9 V14 M10 9 V14 M13 9 V14" stroke="#fff" stroke-width="1.4"/>
  </svg>
  <div class="abs cart-count">0</div>
</nav>

<header>
  <div class="abs navband"></div>
  <div class="abs brand"><span class="brand-square"></span><span class="brand-name">Verdant Sensorik</span></div>
  <nav class="nav">
    <a class="active" style="left:350px">Home</a>
    <a style="left:418px">About</a>
    <a style="left:486px">Products</a>
    <a style="left:576px">Contacts</a>
  </nav>
  <div class="abs search">Search Product
    <svg width="13" height="13" viewBox="0 0 13 13" aria-hidden="true"><circle cx="5.5" cy="5.5" r="4" fill="none" stroke="#0b0b6b" stroke-width="2"/><path d="M8.5 8.5 L12 12" stroke="#0b0b6b" stroke-width="2.4"/></svg>
  </div>
</header>

<section>
  <div class="abs hero" role="img" aria-label="Park with palm trees and a green-tinted modern office building"></div>
  <h1 class="abs hero-title">VERDANT SENSORIK</h1>
  <p class="abs hero-sub">LOREM IPSUM DOLOR SIT AMET</p>
</section>

<section>
  <div class="abs band"></div>
  <article class="abs card" style="left:114px">
    <div class="card-media" role="img" aria-label="Temperature sensor probe with metal head"></div>
    <h3>CONTROLS</h3><div class="rule"></div>
    <p>Lorem ipsum dolor sit amet, consectetur adipiscing elit. Duis ante massa, tristique a eleifend eget</p>
    <div class="btn">VIEW ALL PRODUCTS</div>
  </article>
  <article class="abs card" style="left:443px">
    <div class="card-media" role="img" aria-label="Temperature sensor probe with metal head"></div>
    <h3>CONTROLS</h3><div class="rule"></div>
    <p>Lorem ipsum dolor sit amet, consectetur adipiscing elit. Duis ante massa, tristique a eleifend eget</p>
    <div class="btn">VIEW ALL PRODUCTS</div>
  </article>
  <article class="abs card" style="left:770px">
    <div class="card-media" role="img" aria-label="Temperature sensor probe with metal head"></div>
    <h3>CONTROLS</h3><div class="rule"></div>
    <p>Lorem ipsum dolor sit amet, consectetur adipiscing elit. Duis ante massa, tristique a eleifend eget</p>
    <div class="btn">VIEW ALL PRODUCTS</div>
  </article>
</section>

<section class="welcome">
  <div class="abs welcome-media" role="img" aria-label="Cartoon illustration of a blue temperature sensor"></div>
  <h2>Welcome to Verdant Sensorik</h2>
  <div class="rule"></div>
  <p class="lead">Nulla vitae magna non augue feugiat consectetur at non tortor</p>
  <p class="body">Sed nec fermentum turpis, finibus blandit lorem. Nullam eu blandit sapien. Proin tristique ligula mattis justo sollicitudin, ac tristique sem varius. Maecenas non auctor enim, in faucibus ex. Aliquam elementum mi non ex ultrices cursus. Praesent molestie eleifend turpis, eu dignissim metus dapibus quis. Nullam in molestie tortor. Sed dolor massa, gravida non enim id, sollicitudin eleifend leo. Curabitur ornare porttitor interdum. Maecenas sed ex nibh. Aliquam ultricies risus purus, et facilisis ipsum sodales et. Nullam gravida mauris ac eros tristique, eu scelerisque lectus elementum. Vestibulum quis pharetra libero, quis pretium ex. Ut molestie dolor eros, vitae porta quam lacinia in.</p>
</section>

<section>
  <div class="abs news"></div>
  <svg class="abs" style="left:178px;top:915px" width="33" height="26" viewBox="0 0 33 26" aria-hidden="true">
    <rect x="0" y="0" width="33" height="26" rx="4" fill="#fff"/>
    <path d="M1 3 L16.5 14 L32 3" fill="none" stroke="#2ea200" stroke-width="2.4"/>
  </svg>
  <p class="abs news-text">SUBSCRIBE TO OUR NEWSLETTER TO RECEIVE<br>LOREM IPSUM DOLOR SIT AMET.</p>
  <div class="abs email">Email Address</div>
  <div class="abs subscribe">SUBSCRIBE</div>
</section>

<footer>
  <div class="abs footer"></div>
  <div class="abs flinks" style="left:184px;top:1030px">Home<br>About<br>Products<br>Contacts</div>
  <div class="abs flinks" style="left:361px;top:1030px">Checkout<br>Delivery<br>Help</div>
  <div class="social">
    <i style="top:1039px"></i><span style="top:1036px">Pagebook</span>
    <i style="top:1075px"></i><span style="top:1072px">Chirper</span>
    <i style="top:1111px"></i><span style="top:1108px">Worknet</span>
  </div>
  <svg class="abs" style="left:798px;top:1027px" width="24" height="24" viewBox="0 0 24 24" aria-hidden="true">
    <path d="M6.6 10.8c1.4 2.8 3.8 5.1 6.6 6.6l2.2-2.2c.3-.3.7-.4 1-.2 1.1.4 2.3.6 3.6.6.6 0 1 .4 1 1V20c0 .6-.4 1-1 1C10.6 21 3 13.4 3 4c0-.6.4-1 1-1h3.5c.6 0 1 .4 1 1 0 1.3.2 2.5.6 3.6.1.3 0 .7-.2 1z" fill="#2ea200"/>
  </svg>
  <p class="abs call-label">CALL US:</p>
  <p class="abs call-num">1800 -555-0142</p>
  <svg class="abs" style="left:800px;top:1088px" width="17" height="25" viewBox="0 0 17 25" aria-hidden="true">
    <path d="M8.5 0C3.8 0 0 3.8 0 8.5 0 14.5 8.5 25 8.5 25S17 14.5 17 8.5C17 3.8 13.2 0 8.5 0z" fill="#2ea200"/>
    <circle cx="8.5" cy="8.5" r="3.2" fill="#1b1b2d"/>
  </svg>
  <p class="abs addr">1234 Lorem ipsum dolor sit amet,<br>consectetur adipiscing elit<br>United States</p>
  <div class="abs divider"></div>
  <p class="abs copy">Copyright 2016 Thermolane.com All Rights Reserved.</p>
</footer>

</body>
</html>
```